I need a cover designed for a leadership book to fit my brand of my podcast, Chat with Your Druggist, www.remedyguidance-hub.com, with blues and greens and a professional look since it will be for a professional audience of pharmacists.

Some ideas for an image for the cover might be a woman's hand holding a compass with a road, but I welcome other ideas.

Title of the book is
"Where Chemists Steer: Insights from Ladies [in Focus] Who Are Guiding, Thriving, and Shaping Dispensaries"

```html
<!DOCTYPE html>
<html lang="en">
<head>
<meta charset="utf-8">
<title>Where Chemists Steer – Book Cover</title>
<link rel="stylesheet" href="https://fonts.googleapis.com/css2?family=Oswald:wght@400;500;700&family=Roboto:wght@400&display=swap">
<style>
  :root {
    --back-blue: #356396;
    --back-blue-deep: #2c5687;
    --spine-green: #5dbb46;
    --white: #ffffff;
    --ink-soft: #e9eef5;
    --sky: #a9bccb;
    --sky-haze: #c9cfcf;
    --hills: #c99f66;
    --hills-deep: #a9804e;
    --road: #7a7774;
    --road-dark: #55524f;
  }
  * { box-sizing: border-box; margin: 0; padding: 0; }
  html, body { width: 1200px; height: 900px; overflow: hidden; background: #ffffff; }
  .cover-spread { position: relative; width: 1200px; height: 900px; display: flex; }

  /* Back cover */
  .back-cover {
    position: relative; width: 570px; height: 900px;
    background: var(--back-blue); color: var(--white); overflow: hidden;
  }
  .back-decoration {
    position: absolute; left: -150px; top: 470px; width: 560px; height: 560px; border-radius: 50%;
    background: radial-gradient(circle, rgba(44,86,135,0.9) 0%, rgba(44,86,135,0.55) 45%, rgba(53,99,150,0) 70%);
  }
  .back-title {
    position: absolute; top: 26px; left: 0; width: 570px; text-align: center;
    font-family: "Oswald", sans-serif; font-weight: 700; font-size: 58px; line-height: 1;
    letter-spacing: -0.5px; text-transform: uppercase;
  }
  .back-tagline {
    position: absolute; top: 88px; left: 0; width: 570px; text-align: center;
    font-family: "Oswald", sans-serif; font-weight: 400; font-size: 30px; line-height: 1;
    text-transform: uppercase; letter-spacing: -0.3px;
  }
  .back-rule { position: absolute; top: 126px; left: 136px; }
  .back-blurb {
    position: absolute; top: 147px; left: 34px; width: 505px;
    font-family: "Roboto", sans-serif; font-size: 17px; line-height: 23.3px; color: var(--ink-soft);
  }
  .back-blurb p + p { margin-top: 23.3px; }
  .brand-mark {
    position: absolute; left: 34px; top: 734px; width: 160px;
    display: flex; flex-direction: column; align-items: center; gap: 12px;
  }
  .brand-dot { width: 50px; height: 50px; border-radius: 50%; background: var(--white); }
  .brand-name {
    font-family: "Roboto", sans-serif; font-size: 18px; line-height: 1.2; text-align: center;
    text-transform: uppercase; color: var(--white);
  }
  .barcode-area { position: absolute; left: 340px; top: 734px; width: 200px; height: 120px; background: var(--white); }

  /* Spine */
  .spine {
    position: relative; width: 60px; height: 900px; background: var(--spine-green);
    display: flex; flex-direction: column; align-items: center;
  }
  .spine-title, .spine-author {
    writing-mode: vertical-rl; color: var(--white); text-transform: uppercase;
    font-family: "Oswald", sans-serif; line-height: 1;
  }
  .spine-title { position: absolute; top: 30px; font-weight: 700; font-size: 40px; letter-spacing: -0.5px; }
  .spine-dot { position: absolute; top: 482px; width: 56px; height: 56px; border-radius: 50%; background: var(--white); border: 2px solid #3a6fa5; }
  .spine-author { position: absolute; top: 600px; font-weight: 400; font-size: 34px; letter-spacing: -0.5px; }

  /* Front cover */
  .front-cover { position: relative; width: 570px; height: 900px; overflow: hidden; }
  .front-photo {
    position: absolute; inset: 0;
    background:
      linear-gradient(180deg, var(--sky) 0%, var(--sky-haze) 30%, var(--hills) 38%, var(--hills-deep) 48%, var(--road) 60%, var(--road-dark) 100%);
  }
  .front-title {
    position: absolute; top: 20px; left: 20px;
    font-family: "Oswald", sans-serif; font-weight: 700; font-size: 112px; line-height: 98px;
    color: var(--white); text-transform: uppercase; letter-spacing: -1px;
    text-shadow: 0 2px 6px rgba(0,0,0,0.25);
  }
  .front-subtitle {
    position: absolute; top: 338px; left: 40px; width: 520px; text-align: center;
    font-family: "Oswald", sans-serif; font-weight: 500; font-size: 30px; line-height: 42px;
    color: var(--white); letter-spacing: -0.8px;
    text-shadow: 0 2px 4px rgba(0,0,0,0.55);
  }
  .front-author {
    position: absolute; top: 815px; left: 0; width: 570px; text-align: center;
    font-family: "Oswald", sans-serif; font-weight: 400; font-size: 36px; line-height: 1;
    color: var(--white); text-transform: uppercase; letter-spacing: -0.8px;
    text-shadow: 0 2px 4px rgba(0,0,0,0.5);
  }
</style>
</head>
<body>
<main class="cover-spread">
  <section class="back-cover">
    <div class="back-decoration" role="img" aria-label="Faint compass rose decoration"></div>
    <h2 class="back-title">Where Chemists Steer</h2>
    <p class="back-tagline">Chat with Your Druggist</p>
    <svg class="back-rule" width="298" height="4" viewBox="0 0 298 4" aria-hidden="true">
      <path d="M0 2 Q149 0 298 2 Q149 4 0 2Z" fill="#ffffff"/>
    </svg>
    <div class="back-blurb">
      <p>Lorem ipsum dolor sit amet, consectetur adipisicing elit, sed do eiusmod tempor incididunt ut labore et dolore magna aliqua. Ut enim ad minim veniam, quis nostrud exercitation ullamco laboris nisi ut aliquip ex ea commodo consequat.</p>
      <p>Duis aute irure dolor in reprehenderit in voluptate velit esse cillum dolore eu fugiat nulla pariatur. Excepteur sint occæcat cupidatat non proident, sunt in culpa qui officia deserunt mollit anim id est laborum. Sed ut perspiciatis unde omnis iste natus error sit voluptatem accusantium doloremque laudantium, totam rem aperiam, eaque ipsa quæ ab illo inventore veritatis et quasi architecto beatæ vitæ dicta sunt explicabo.</p>
      <p>Nemo enim ipsam voluptatem quia voluptas sit aspernatur aut odit aut fugit, sed quia consequuntur magni dolores eos qui ratione voluptatem sequi nesciunt. Neque porro quisquam est, qui dolorem ipsum quia dolor sit amet, consectetur, adipisci velit, sed quia non numquam eius modi tempora incidunt ut labore et dolore magnam aliquam quærat voluptatem.</p>
    </div>
    <div class="brand-mark">
      <span class="brand-dot"></span>
      <span class="brand-name">Chat with Your Druggist</span>
    </div>
    <div class="barcode-area"></div>
  </section>

  <section class="spine">
    <span class="spine-title">Where Chemists Steer</span>
    <span class="spine-dot"></span>
    <span class="spine-author">Marlena Whitcombe</span>
  </section>

  <section class="front-cover">
    <div class="front-photo" role="img" aria-label="Photo of a woman's hand holding a compass over an open road through golden hills"></div>
    <h1 class="front-title">Where<br>Chemists<br>Steer</h1>
    <p class="front-subtitle">Insights from Ladies [in Focus] Who Are Guiding, Thriving, and Shaping Dispensaries</p>
    <p class="front-author">By Marlena Whitcombe PharmD, MBA</p>
  </section>
</main>
</body>
</html>
```